business card

Business card for new business.
Red and black corporate colors.
Card can have an Indsutrial feel to it. Feel free to add Rust, Bolted steel, or graphics as you see fit. We provide highly specialized services to the below mentioned industries.
Keep information out of corners so that if I want I can choose rounded corners.
Information
- front. name - title - phone - email
- Rear
Pipelines - Ports - Construction - Forestry - Utilities
Ridgemont - Larkfield - Port Halden - Stonebrook - Westhaven

```html
<!DOCTYPE html>
<html lang="en">
<head>
<meta charset="utf-8">
<title>Girderline Business Card</title>
<link rel="stylesheet" href="https://fonts.googleapis.com/css2?family=Roboto:wght@400;500&family=Roboto+Condensed:wght@700&display=swap">
<style>
  :root {
    --backdrop: #5a4838;
    --brand-red: #e30018;
    --paper: #f2f2f2;
    --white: #ffffff;
    --logo-grey: #7d7d7d;
    --text-grey: #4a4a4a;
  }
  * { margin: 0; padding: 0; box-sizing: border-box; }
  html, body {
    width: 1200px;
    height: 960px;
    overflow: hidden;
    background: var(--backdrop);
  }
  .canvas {
    position: relative;
    width: 1200px;
    height: 960px;
  }
  .card {
    position: absolute;
    width: 600px;
    height: 342px;
    box-shadow: 2px 3px 4px rgba(0, 0, 0, 0.45);
  }
  .card--front {
    left: 313px;
    top: 114px;
    background: var(--brand-red);
    color: var(--white);
    font-family: "Roboto", Arial, sans-serif;
  }
  .card--back {
    left: 311px;
    top: 472px;
    background: var(--paper);
    font-family: "Roboto", Arial, sans-serif;
  }
  .identity {
    position: absolute;
    left: 44px;
    top: 228px;
    display: flex;
    align-items: baseline;
  }
  .identity__name {
    font-family: "Roboto Condensed", "Arial Narrow", sans-serif;
    font-weight: 700;
    font-size: 21px;
    letter-spacing: 0.2px;
  }
  .identity__title {
    margin-left: 8px;
    padding-left: 7px;
    border-left: 1px solid var(--white);
    font-size: 15px;
    line-height: 15px;
  }
  .contact {
    position: absolute;
    left: 44px;
    top: 263px;
    font-size: 14.5px;
    line-height: 20px;
  }
  .wordmark {
    position: absolute;
    left: 259px;
    top: 177px;
    width: 300px;
    display: flex;
    align-items: center;
    justify-content: center;
    gap: 12px;
  }
  .wordmark__square {
    width: 22px;
    height: 22px;
    background: var(--brand-red);
  }
  .wordmark__name {
    font-family: "Roboto Condensed", "Arial Narrow", sans-serif;
    font-weight: 700;
    font-size: 50px;
    line-height: 56px;
    color: var(--logo-grey);
  }
  .coverage {
    position: absolute;
    right: 41px;
    top: 261px;
    text-align: right;
    font-size: 14.5px;
    line-height: 18px;
    color: var(--text-grey);
  }
  .coverage__sep { color: var(--brand-red); }
</style>
</head>
<body>
<main class="canvas">
  <section class="card card--front" aria-label="Card front">
    <div class="identity">
      <span class="identity__name">ALEX MORGAN</span>
      <span class="identity__title">CEO/FOUNDER</span>
    </div>
    <div class="contact">
      <p class="contact__phone">555 014 2290</p>
      <p class="contact__web">info@girderline.com | www.girderline.com</p>
    </div>
  </section>

  <section class="card card--back" aria-label="Card back">
    <div class="wordmark">
      <span class="wordmark__square"></span>
      <span class="wordmark__name">GIRDERLINE</span>
    </div>
    <div class="coverage">
      <p>Pipelines<span class="coverage__sep">–</span>Ports<span class="coverage__sep">–</span>Construction<span class="coverage__sep">–</span>Forestry</p>
      <p>Utilities<span class="coverage__sep">–</span>Ridgemont<span class="coverage__sep">–</span>Larkfield<span class="coverage__sep">–</span>Port Halden</p>
      <p>Stonebrook<span class="coverage__sep">–</span>Westhaven</p>
    </div>
  </section>
</main>
</body>
</html>
```